Maple. Step PT Tri-Fold

An on demand house call mobile physical therapy and wellness company. Focused on quality rehabilitation management health and wellness needs to your door.
We need a tri-fold brochure to describe our services

Target Market(s)

Patients in need of physical therapy

Industry/Entity Type

Physical Therapy

Font styles to use
Serif
Sans Serif
Other font styles liked:
• Attached is some necessary content from a prior brochure

Colors
0054AA
0677BA
7BADD7
CADEEF
E8F1F8
EB3D1F
EC4F4E
F09395
F8D3D4
FCEDEE

```html
<!DOCTYPE html>
<html lang="en">
<head>
<meta charset="utf-8">
<title>Maple. Step PT Tri-Fold</title>
<link rel="stylesheet" href="https://fonts.googleapis.com/css2?family=Montserrat:ital,wght@0,400;0,500;0,600;0,700;0,800;1,600&family=Raleway:wght@400;500;600&display=swap">
<style>
:root{
  --blue-deep:#0054AA;
  --blue:#0677BA;
  --blue-mid:#1a72b8;
  --blue-soft:#7BADD7;
  --blue-pale:#CADEEF;
  --red:#EC4F4E;
  --red-strong:#EB3D1F;
  --pink:#F8D3D4;
  --stage:#a9a9a9;
  --paper:#ffffff;
  --panel-grey:#f3f3f3;
  --text:#555b63;
  --light-text:#dfe4ea;
}
*{margin:0;padding:0;box-sizing:border-box}
html,body{width:959px;height:1200px;overflow:hidden;background:var(--stage)}
body{position:relative;font-family:'Raleway',sans-serif;color:var(--text)}
.sheet{position:absolute;background:var(--paper);overflow:hidden;box-shadow:0 2px 6px rgba(0,0,0,.25)}
.sheet--outside{left:125px;top:77px;width:708px;height:500px}
.sheet--inside{left:127px;top:621px;width:709px;height:501px}
.panel{position:absolute;top:0;height:100%}

/* outside: intro panel */
.intro{left:0;width:236px;background:var(--panel-grey)}
.photo{position:absolute}
.intro .photo{left:0;top:0;width:236px;height:158px;background:linear-gradient(160deg,#e9eef3 0%,#c9d4de 45%,#b78a5c 100%)}
.intro .rule{position:absolute;left:0;top:158px;width:236px;height:4px;background:var(--red)}
.intro .lead{position:absolute;left:20px;top:177px;width:196px;font-size:8.4px;line-height:11.2px;text-align:justify}
.benefits{position:absolute;left:20px;top:247px;width:180px;list-style:none}
.benefits li{position:relative;padding-left:17px;font-size:8.1px;line-height:11px;margin-bottom:6.4px}
.benefits svg{position:absolute;left:0;top:2px;width:8px;height:8px}

/* outside: contact panel */
.contact{left:236px;width:236px;background:linear-gradient(180deg,var(--blue-mid) 0%,#0f64aa 100%);text-align:center;color:var(--light-text)}
.contact .brand-mark{position:absolute;left:0;right:0;top:88px;display:flex;justify-content:center}
.contact .brand-mark span{width:22px;height:22px;border:2px solid var(--light-text);border-radius:50%}
.contact .brand-name{position:absolute;left:0;right:0;top:148px;font-family:'Montserrat',sans-serif;font-weight:600;font-size:22px}
.divider{position:absolute;left:108px;width:26px;height:1.5px;background:var(--light-text)}
.contact .details{position:absolute;left:0;right:0;top:214px;font-size:15px;line-height:21.5px;font-weight:500}
.socials{position:absolute;left:0;right:0;top:318px;display:flex;justify-content:center;gap:3px}
.socials span{width:18px;height:18px;border-radius:50%;background:var(--light-text)}
.contact .web{position:absolute;left:0;right:0;top:365px;font-family:'Montserrat',sans-serif;font-size:15.5px;font-weight:600}

/* outside: cover panel */
.cover{left:472px;width:236px;background:var(--paper);overflow:visible}
.cover .brand{position:absolute;left:0;right:0;top:30px;display:flex;align-items:center;justify-content:center;gap:7px;font-family:'Montserrat',sans-serif;font-weight:700;font-size:18.5px;color:var(--blue)}
.cover .brand span{width:16px;height:16px;border-radius:50%;background:var(--red)}
.cover .photo{left:0;top:74px;width:236px;height:426px;background:linear-gradient(135deg,#ecebe6 0%,#d9cfc4 40%,#5a8fb6 75%,#2f6b9a 100%)}
.cover-block{position:absolute;left:-36px;top:270px;width:272px;height:230px}
.cover-text{position:absolute;left:0;right:0;top:387px;text-align:center;color:#fff;font-family:'Montserrat',sans-serif}
.cover-text h1{font-size:18px;font-weight:800;line-height:20px}
.cover-text .sub{font-size:10.6px;font-weight:700;line-height:12px}
.cover-text .tag{margin-top:5px;font-size:9.6px;font-style:italic;font-weight:600}
.cover-text .web{margin-top:14px;font-size:10px;font-weight:500;letter-spacing:2.4px}

/* inside: insurances */
.insurance{left:0;width:235px;background:linear-gradient(135deg,var(--blue) 0%,#0b5a9e 100%);color:#fff}
.tab{position:absolute;font-family:'Montserrat',sans-serif;font-weight:800;border-radius:3px;text-align:center}
.insurance .tab{left:11px;top:21px;width:214px;height:26px;line-height:26px;font-size:13.5px;background:var(--red);color:#fde6e6}
.insurance .note{position:absolute;left:22px;top:60px;font-family:'Montserrat',sans-serif;font-weight:700;font-size:11px;line-height:14.5px}
.plans{position:absolute;left:22px;top:97px;list-style:none}
.plans li{position:relative;padding-left:18px;font-size:11.3px;font-weight:500;height:21.8px;line-height:18px}
.plans svg{position:absolute;left:0;top:5px;width:8px;height:8px}
.call{position:absolute;left:15px;top:396px;width:208px;height:79px;background:var(--red);border-radius:7px;text-align:center;color:#fde6e6;font-family:'Montserrat',sans-serif;font-weight:700}
.call .head{padding-top:4px;font-size:19.5px}
.call .num{font-size:22px;line-height:25px}
.call .web{font-size:14px;letter-spacing:2px;font-weight:600}

/* inside: programs */
.programs{left:235px;width:234px;background:var(--paper)}
.programs .tab{left:13px;top:23px;width:213px;height:26px;line-height:26px;font-size:13px;background:var(--blue-deep);color:#fff}
.tile{position:absolute;width:133px;height:82px}
.tile .shot{position:absolute;left:0;top:0;width:100%;height:65px}
.tile .label{position:absolute;left:0;bottom:0;width:100%;height:17px;background:var(--red);color:#fff;font-family:'Montserrat',sans-serif;font-size:7px;font-weight:600;display:flex;align-items:center;justify-content:center;text-align:center;line-height:8px}
.tile--tall .shot{height:62px}
.tile--tall .label{height:20px}
.programs .tile{left:47px}
.programs .brand-name{position:absolute;left:0;right:0;top:457px;text-align:center;font-family:'Montserrat',sans-serif;font-weight:700;font-size:21px;color:var(--blue)}

/* inside: more programs */
.more{left:469px;width:240px;background:linear-gradient(90deg,#bdbdbd 0%,#dcdcdc 15%,#e4e4e4 100%)}
.more .tile{left:50px}
</style>
</head>
<body>

<section class="sheet sheet--outside">
  <div class="panel intro">
    <div class="photo" role="img" aria-label="Senior man exercising with dumbbells in a bright studio"></div>
    <div class="rule"></div>
    <p class="lead">Our home-based outpatient physical therapy delivers high quality therapy services in the comfort of your own home. Patients are not required to be “homebound,” as they would in the home health setting</p>
    <ul class="benefits">
      <li><svg viewBox="0 0 10 10"><circle cx="5" cy="5" r="5" fill="#0677BA"/><path d="M2.8 5.2l1.5 1.5 3-3" stroke="#fff" stroke-width="1.3" fill="none"/></svg>Not having to arrange for someone to drive them to a clinic</li>
      <li><svg viewBox="0 0 10 10"><circle cx="5" cy="5" r="5" fill="#0677BA"/><path d="M2.8 5.2l1.5 1.5 3-3" stroke="#fff" stroke-width="1.3" fill="none"/></svg>The privacy that comes from one-on-one care</li>
      <li><svg viewBox="0 0 10 10"><circle cx="5" cy="5" r="5" fill="#0677BA"/><path d="M2.8 5.2l1.5 1.5 3-3" stroke="#fff" stroke-width="1.3" fill="none"/></svg>Building a treatment plan around how they live</li>
      <li><svg viewBox="0 0 10 10"><circle cx="5" cy="5" r="5" fill="#0677BA"/><path d="M2.8 5.2l1.5 1.5 3-3" stroke="#fff" stroke-width="1.3" fill="none"/></svg>The use of the home to provide space for exercise in order to build commitment to a home exercise plan</li>
      <li><svg viewBox="0 0 10 10"><circle cx="5" cy="5" r="5" fill="#0677BA"/><path d="M2.8 5.2l1.5 1.5 3-3" stroke="#fff" stroke-width="1.3" fill="none"/></svg>The sense of independence gained from getting better and gaining function in the home</li>
      <li><svg viewBox="0 0 10 10"><circle cx="5" cy="5" r="5" fill="#0677BA"/><path d="M2.8 5.2l1.5 1.5 3-3" stroke="#fff" stroke-width="1.3" fill="none"/></svg>The sense of family that comes from knowing you have a skilled clinician who knows the ins and outs of your home and your loved one’s challenges and can be reached when you need them.</li>
    </ul>
  </div>

  <div class="panel contact">
    <div class="brand-mark"><span></span></div>
    <div class="brand-name">Maple. Step PT</div>
    <div class="divider" style="top:193px"></div>
    <div class="details">(555) 214-7720<br>hello@maplesteppt.com<br>(555) 214-7731</div>
    <div class="divider" style="top:298px"></div>
    <div class="socials"><span></span><span></span><span></span></div>
    <div class="web">www.maplesteppt.com</div>
  </div>

  <div class="panel cover">
    <div class="brand"><span></span>Maple. Step PT</div>
    <div class="photo" role="img" aria-label="Therapist helping a smiling senior man lift hand weights from a wheelchair"></div>
    <svg class="cover-block" viewBox="0 0 272 230" aria-hidden="true"><path d="M0 230 L0 150 L150 0 L272 0 L272 230 Z" fill="#EC4F4E" opacity=".96"/></svg>
    <div class="cover-text">
      <h1>PHYSICAL THERAPY</h1>
      <p class="sub">Delivered to you Finding the right<br>Rehabilitation Shapes Recovery</p>
      <p class="tag">Convenient support &amp; expert therapist</p>
      <p class="web">WWW.MAPLESTEPPT.COM</p>
    </div>
  </div>
</section>

<section class="sheet sheet--inside">
  <div class="panel insurance">
    <div class="tab">ACCEPTED INSURANCES</div>
    <p class="note">Incudes all ADVANTAGE, LTC, &amp;<br>STATECARE plans</p>
    <ul class="plans">
      <li><svg viewBox="0 0 10 10"><circle cx="5" cy="5" r="5" fill="#fff"/><path d="M2.8 5.2l1.5 1.5 3-3" stroke="#0677BA" stroke-width="1.3" fill="none"/></svg>Unity Health Cover</li>
      <li><svg viewBox="0 0 10 10"><circle cx="5" cy="5" r="5" fill="#fff"/><path d="M2.8 5.2l1.5 1.5 3-3" stroke="#0677BA" stroke-width="1.3" fill="none"/></svg>Commons Care Plan</li>
      <li><svg viewBox="0 0 10 10"><circle cx="5" cy="5" r="5" fill="#fff"/><path d="M2.8 5.2l1.5 1.5 3-3" stroke="#0677BA" stroke-width="1.3" fill="none"/></svg>Everwell Care</li>
      <li><svg viewBox="0 0 10 10"><circle cx="5" cy="5" r="5" fill="#fff"/><path d="M2.8 5.2l1.5 1.5 3-3" stroke="#0677BA" stroke-width="1.3" fill="none"/></svg>Mesa Valley Health Plan</li>
      <li><svg viewBox="0 0 10 10"><circle cx="5" cy="5" r="5" fill="#fff"/><path d="M2.8 5.2l1.5 1.5 3-3" stroke="#0677BA" stroke-width="1.3" fill="none"/></svg>Campus Family Care</li>
      <li><svg viewBox="0 0 10 10"><circle cx="5" cy="5" r="5" fill="#fff"/><path d="M2.8 5.2l1.5 1.5 3-3" stroke="#0677BA" stroke-width="1.3" fill="none"/></svg>Wellnet</li>
      <li><svg viewBox="0 0 10 10"><circle cx="5" cy="5" r="5" fill="#fff"/><path d="M2.8 5.2l1.5 1.5 3-3" stroke="#0677BA" stroke-width="1.3" fill="none"/></svg>Shieldcross &amp; Senior Net</li>
      <li><svg viewBox="0 0 10 10"><circle cx="5" cy="5" r="5" fill="#fff"/><path d="M2.8 5.2l1.5 1.5 3-3" stroke="#0677BA" stroke-width="1.3" fill="none"/></svg>Brookway</li>
      <li><svg viewBox="0 0 10 10"><circle cx="5" cy="5" r="5" fill="#fff"/><path d="M2.8 5.2l1.5 1.5 3-3" stroke="#0677BA" stroke-width="1.3" fill="none"/></svg>Kindly Care</li>
      <li><svg viewBox="0 0 10 10"><circle cx="5" cy="5" r="5" fill="#fff"/><path d="M2.8 5.2l1.5 1.5 3-3" stroke="#0677BA" stroke-width="1.3" fill="none"/></svg>KindlyMesa</li>
      <li><svg viewBox="0 0 10 10"><circle cx="5" cy="5" r="5" fill="#fff"/><path d="M2.8 5.2l1.5 1.5 3-3" stroke="#0677BA" stroke-width="1.3" fill="none"/></svg>SeniorCover</li>
      <li><svg viewBox="0 0 10 10"><circle cx="5" cy="5" r="5" fill="#fff"/><path d="M2.8 5.2l1.5 1.5 3-3" stroke="#0677BA" stroke-width="1.3" fill="none"/></svg>TriServe</li>
      <li><svg viewBox="0 0 10 10"><circle cx="5" cy="5" r="5" fill="#fff"/><path d="M2.8 5.2l1.5 1.5 3-3" stroke="#0677BA" stroke-width="1.3" fill="none"/></svg>Tribal Health Services (THS)</li>
    </ul>
    <div class="call">
      <p class="head">CALL US TODAY</p>
      <p class="num">(555) 214-7720</p>
      <p class="web">www.maplesteppt.com</p>
    </div>
  </div>

  <div class="panel programs">
    <div class="tab">REHABILITATION PROGRAMS</div>
    <div class="tile" style="top:66px"><div class="shot" role="img" aria-label="Therapist working with a senior man in a living room" style="background:linear-gradient(135deg,#d8d1c7,#3f78a8)"></div><div class="label">GERIATRICS</div></div>
    <div class="tile" style="top:162px"><div class="shot" role="img" aria-label="Patient walking between parallel bars with a therapist" style="background:linear-gradient(135deg,#f1f1f1,#d9dde2 60%,#c94f8a)"></div><div class="label">NEUROLOGICAL</div></div>
    <div class="tile" style="top:258px"><div class="shot" role="img" aria-label="Kinesiology tape applied to a knee" style="background:linear-gradient(135deg,#e9c3ac,#d59a83 55%,#e95c9a)"></div><div class="label">ORTHOPEDICS</div></div>
    <div class="tile" style="top:354px"><div class="shot" role="img" aria-label="Patient exercising on a rehab machine with a trainer" style="background:linear-gradient(135deg,#e6e9ec,#c9d3dc 55%,#e98b8b)"></div><div class="label">POST-OPERATIVE</div></div>
    <div class="brand-name">Maple. Step PT</div>
  </div>

  <div class="panel more">
    <div class="tile" style="top:21px"><div class="shot" role="img" aria-label="Trainer guiding a woman on an exercise ball" style="background:linear-gradient(135deg,#f2f2f2,#c7c2bd 60%,#6d5a50)"></div><div class="label">SPORTS MEDICINE</div></div>
    <div class="tile" style="top:117px"><div class="shot" role="img" aria-label="Foot stepping on a balance board" style="background:linear-gradient(135deg,#9aa3ad,#c99a70 70%,#d8b48e)"></div><div class="label">BALANCE/VESTIBULAR</div></div>
    <div class="tile" style="top:213px"><div class="shot" role="img" aria-label="Person walking on a treadmill" style="background:linear-gradient(180deg,#fafafa,#e2e2e2)"></div><div class="label">CHF</div></div>
    <div class="tile" style="top:309px"><div class="shot" role="img" aria-label="Senior woman stretching a resistance band" style="background:linear-gradient(135deg,#6f5a52,#d8d2cc 50%,#3a3a58)"></div><div class="label">COPD</div></div>
    <div class="tile tile--tall" style="top:403px"><div class="shot" role="img" aria-label="Nurse supporting a senior woman outdoors" style="background:linear-gradient(135deg,#f3e6e6,#dde6da 55%,#7fa8cf)"></div><div class="label">HOME SAFETY&amp;<br>FALL PREVENTION</div></div>
  </div>
</section>

</body>
</html>
```